Packaging Design Project - Organic Baby Skin Care

This project is to re-design our current organic baby skin care range labels. See here:

http://www.velvetmeadow.com.au/Baby-Care

The common complaint is that the pink is too girly for boys. For this reason I am not sure if I should keep the "Velvet Meadow Baby" Logo as it is a bit girly looking as well. So open to your ideas.

The size of the label will be approx 90 w x 70 h mm

Here is one range I like that is already similar to what I am already doing with the polka dots but in different pastels: http://www.tiptapstore.com/baby-skincare.html

Also another idea for a concept here with a beige/vintage look background: http://www.pinebarnstore.com/tiny_fern_naturals/tiny_fern_naturals_creamy_body_lotion-c482915p730218.html

Lastly, I also like these fun colourful, child like graphics of this range:

http://www.wrenhollownaturals.co.uk/brands/hush-drowsy-bear/

The range consists of:

Soothing Baby Salve in a white tube
Bubbly Fresh Baby Bath in a white 250ml bottle
Nana and Bibi Rubbing Oil in a white 100ml bottle
Quiet Night Relaxing Spray in a white 100ml bottle
Oat Cream Bar in a cardboard box

See packaging attached.

I will be presenting all the designs to a group of mother's for market research so they will be making the final decision - seeing they are the ones who will ultimately buy the product.

That is why I am open to a wide range of styles for this project.

Looking forward to seeing your work!

Any questions, let me know!
Updates

Hello Designers!

I have posted an update to include more information in the brief and also the AI logo file which shows the current packaging. Also images of the bottles of the current range. The bottles will be white boston round bottles not the tall boston as I am currently using.

many thanks

Loretta

Hello Designers

Just wanted to get an update on how you are going with your design submissions?

The deadline is this Saturday and we have received very few designs.

I await your reply.

thanks
Loretta

Reason: The deadline is drawing near and have not received enough designs. Please submit your designs as soon as you can. Many thanks Loretta Velvet Meadow

Target Market(s)

Mothers 25 - 40

Industry/Entity Type

Market Research

Requirements
Must have
• Organic/Natural feel, Stylish, Elegant, Gender Neutral to suit both sexes
Nice to have
• Vintage feel

```html
<!DOCTYPE html>
<html lang="en">
<head>
<meta charset="utf-8">
<title>Nana &amp; Bibi Rubbing Oil – Label</title>
<link rel="stylesheet" href="https://fonts.googleapis.com/css2?family=Merienda:wght@400;700&display=swap">
<style>
  :root {
    --page: #ffffff;
    --band: #a07a9b;
    --band-soft: #b596b0;
    --panel: #fdfcfd;
    --ink: #6a2c7c;
    --art-main: #9a6c97;
    --art-light: #cdb6cb;
    --badge: #f6d7ad;
  }
  html, body {
    margin: 0;
    padding: 0;
    width: 1200px;
    height: 948px;
    overflow: hidden;
    background: var(--page);
  }
  .label {
    position: relative;
    width: 1200px;
    height: 948px;
  }
  .label-shape {
    position: absolute;
    inset: 0;
  }
  .brand {
    position: absolute;
    left: 350px;
    width: 500px;
    top: 150px;
    display: flex;
    flex-direction: column;
    align-items: center;
    gap: 12px;
  }
  .brand-dot {
    width: 100px;
    height: 100px;
    border-radius: 50%;
    background: var(--badge);
  }
  .brand-name {
    margin: 0;
    font-family: "Merienda", cursive;
    font-weight: 700;
    font-size: 20px;
    color: var(--ink);
  }
  .product-name {
    position: absolute;
    left: 350px;
    width: 500px;
    top: 622px;
    margin: 0;
    text-align: center;
    font-family: "Merienda", cursive;
    font-weight: 400;
    font-size: 44px;
    line-height: 58px;
    color: var(--ink);
  }
</style>
</head>
<body>
<main class="label">
  <svg class="label-shape" width="1200" height="948" viewBox="0 0 1200 948" xmlns="http://www.w3.org/2000/svg">
    <defs>
      <pattern id="band-wave-top" x="80" y="52" width="40" height="20" patternUnits="userSpaceOnUse">
        <path d="M0,20 L0,14 C10,14 10,0 20,0 C30,0 30,14 40,14 L40,20 Z" fill="var(--band)"/>
      </pattern>
      <pattern id="band-wave-bottom" x="80" y="876" width="40" height="20" patternUnits="userSpaceOnUse">
        <path d="M0,0 L0,6 C10,6 10,20 20,20 C30,20 30,6 40,6 L40,0 Z" fill="var(--band)"/>
      </pattern>
      <pattern id="panel-teeth-top" x="350" y="104" width="32" height="16" patternUnits="userSpaceOnUse">
        <path d="M0,16 L0,13 C8,13 8,1 16,1 C24,1 24,13 32,13 L32,16 Z" fill="var(--panel)"/>
      </pattern>
      <pattern id="panel-teeth-bottom" x="350" y="828" width="32" height="16" patternUnits="userSpaceOnUse">
        <path d="M0,0 L0,3 C8,3 8,15 16,15 C24,15 24,3 32,3 L32,0 Z" fill="var(--panel)"/>
      </pattern>
      <radialGradient id="band-tone" cx="0.5" cy="0.5" r="0.7">
        <stop offset="0" stop-color="var(--band)"/>
        <stop offset="0.6" stop-color="var(--band-soft)"/>
        <stop offset="1" stop-color="var(--band)"/>
      </radialGradient>
      <linearGradient id="bird-tone" x1="0" y1="0" x2="1" y2="1">
        <stop offset="0" stop-color="var(--art-main)"/>
        <stop offset="1" stop-color="var(--art-light)"/>
      </linearGradient>
    </defs>

    <g class="band">
      <rect x="70" y="68" width="1060" height="812" rx="14" fill="var(--band)"/>
      <rect x="80" y="52" width="1040" height="20" fill="url(#band-wave-top)"/>
      <rect x="80" y="876" width="1040" height="20" fill="url(#band-wave-bottom)"/>
      <rect class="band-pattern-left" x="70" y="72" width="280" height="804"
            fill="url(#band-tone)" role="img"
            aria-label="Small white flowers scattered in rows across the purple band"/>
      <rect class="band-pattern-right" x="850" y="72" width="280" height="804"
            fill="url(#band-tone)" role="img"
            aria-label="Small white flowers scattered in rows across the purple band"/>
    </g>

    <g class="panel">
      <rect x="350" y="118" width="500" height="712" fill="var(--panel)"/>
      <rect x="350" y="104" width="500" height="16" fill="url(#panel-teeth-top)"/>
      <rect x="350" y="828" width="500" height="16" fill="url(#panel-teeth-bottom)"/>
    </g>

    <rect class="bird-art" x="430" y="370" width="340" height="220" rx="60"
          fill="url(#bird-tone)" role="img"
          aria-label="Illustration of a mother bird and a baby bird with patterned wings sitting on a curved branch"/>
  </svg>

  <div class="brand">
    <span class="brand-dot" aria-hidden="true"></span>
    <p class="brand-name">Velvet Meadow Baby</p>
  </div>

  <h1 class="product-name">Nana &amp; Bibi<br>Rubbing Oil</h1>
</main>
</body>
</html>
```